Great Opportunity !! Masters in Business Analytics College Course

the size is Full Page, with bleed*
8”x 10.75" plus 0.25" bleed.
please leave one inch for footer
the purpose is attract students to join this college program .
this is for students in USA .
college age of around 24 years old
I am looking for a flyer that is unique and shows creativity .
A flyer that people would want to look at it because it is unique.
you can choose either vector, text ,or picture.
if you do picture it should be a white USA citizen wearing a white solid shirt and not long hair

Target Market(s)

USA students about 23 in age to join this college program

Industry/Entity Type

education

Colors
0054AA
0677BA
7BADD7
CADEEF
E8F1F8
0094D4
00A9DD
6FCCEA
C7EBF8
E9F6FB

Requirements
Must have
• the text should not be crowded .. .. .. the ad should not be full of text
Should not have
• not have very large text .. it should not be a flyer that is full of text .. you have to figure out how to avoid looking at the ad and it is very busy with text

```html
<!DOCTYPE html>
<html lang="en">
<head>
<meta charset="utf-8">
<title>Harlow State College – Business Analytics Open House</title>
<link href="https://fonts.googleapis.com/css2?family=Inter:wght@400;600;700;800&display=swap" rel="stylesheet">
<style>
  :root{
    --stage:#e4e4e4;
    --paper:#ffffff;
    --blue:#2d6fdc;
    --blue-deep:#2a6bd8;
    --sky-top:#b9defe;
    --sky-bottom:#69a6f4;
    --panel-grey:#f1f1f1;
    --footer-grey:#f6f6f6;
    --ink:#555555;
    --accent-red:#e02020;
  }
  *{box-sizing:border-box;margin:0;padding:0}
  html,body{width:728px;height:1200px;overflow:hidden}
  body{background:var(--stage);font-family:"Inter",Arial,sans-serif;color:var(--ink);letter-spacing:-0.04em}
  .flyer{position:absolute;left:22px;top:144px;width:684px;height:912px;background:var(--paper);box-shadow:0 6px 22px rgba(0,0,0,.18)}
  .flyer > *{position:absolute}

  .hook{left:24px;top:24px;width:236px;height:263px;border-top-left-radius:36px;
        background:linear-gradient(180deg,var(--sky-top),var(--sky-bottom))}
  .hook-arrow{position:absolute;left:172px;top:20px}
  .hook-question{position:absolute;right:17px;top:82px;width:210px;text-align:right;color:#fff;
        font-weight:700;font-size:27px;line-height:33px}

  .details{left:24px;top:300px;width:236px;height:504px;background:var(--panel-grey);border-bottom-right-radius:36px;padding:22px 0 0 25px;overflow:hidden}
  .open-house{color:var(--blue);font-weight:800;font-size:51px;line-height:47px;letter-spacing:-0.05em}
  .date{margin-top:20px;font-weight:700;font-size:23px;line-height:26px;color:var(--ink)}
  .contact{margin-top:18px;font-size:19px;line-height:23px}
  .contact .email{color:var(--blue);font-weight:700;letter-spacing:-0.05em;white-space:nowrap}
  .note{margin-top:25px;font-size:18px;line-height:23px;padding-right:12px}
  .note .mark{color:var(--accent-red);font-size:14px;vertical-align:top}
  .format{margin-top:17px;font-size:18px;line-height:23px;padding-right:12px}

  .headline{left:280px;top:40px;width:390px;color:var(--blue);font-weight:700;font-size:37px;line-height:36px;letter-spacing:-0.05em}
  .headline .mark{color:var(--accent-red)}
  .subhead{left:280px;top:160px;width:360px;font-weight:700;font-size:23px;line-height:27px;color:var(--ink)}

  .salary-band{left:269px;top:231px;width:391px;height:56px;background:var(--blue-deep);border-bottom-right-radius:26px;
        color:#fff;font-weight:700;font-size:22px;line-height:56px;padding-left:10px;white-space:nowrap}
  .source{left:279px;top:298px;font-size:19px;color:var(--ink)}

  .job-list{top:338px;list-style:none;font-size:18px;line-height:26.5px;white-space:nowrap}
  .job-list.col-a{left:270px}
  .job-list.col-b{left:423px}
  .job-list li,.hire-list li{display:flex;align-items:center;gap:12px}
  .tick{flex:none}

  .portrait{left:269px;top:441px;width:237px;height:363px;border-top-right-radius:36px;
        background:linear-gradient(180deg,#bfe0fd 0%,#93c3fa 55%,#6ea8f4 100%)}
  .chevrons{left:520px;top:453px}
  .hired-title{left:521px;top:549px;color:var(--blue);font-weight:700;font-size:24px;line-height:28px}
  .hire-list{left:521px;top:640px;list-style:none;font-size:22px;line-height:32px;color:var(--ink)}

  .footer-band{left:11px;top:817px;width:662px;height:83px;background:var(--footer-grey)}
</style>
</head>
<body>
<svg width="0" height="0" style="position:absolute">
  <symbol id="tick-mark" viewBox="0 0 14 12"><path d="M1.5 6.5 L5 10 L12.5 1.5" fill="none" stroke="#2d6fdc" stroke-width="1.8" stroke-linecap="round" stroke-linejoin="round"/></symbol>
</svg>

<main class="flyer">
  <section class="hook">
    <svg class="hook-arrow" width="46" height="50" viewBox="0 0 46 50">
      <path d="M3 48 C4 26 18 12 40 10" fill="none" stroke="#fff" stroke-width="3" stroke-linecap="round"/>
      <path d="M31 3 L41 10 L33 19" fill="none" stroke="#fff" stroke-width="3" stroke-linecap="round" stroke-linejoin="round"/>
    </svg>
    <p class="hook-question">Do you have an analytical mind and are seeking a profitable career?</p>
  </section>

  <section class="details">
    <h2 class="open-house">Open<br>House</h2>
    <p class="date">Wednesday,<br>April 20, 7:30 pm.</p>
    <p class="contact">Email<br><span class="email">info@harlowsc.edu</span><br>for the link!</p>
    <p class="note"><span class="mark">**</span> Harlow State College "Only 5% of universities achieve prestigious ABEQ accreditation."</p>
    <p class="format">21 months<br>Hybrid with one weekly in-person evening meeting</p>
  </section>

  <h1 class="headline">A Master's in Business Analytics from Harlow State College<span class="mark">**</span></h1>
  <p class="subhead">can prepare you for some of the most in-demand jobs.</p>

  <div class="salary-band">Jobs with a median salary of $100k+</div>
  <p class="source">(National Labor Data Office 2023)</p>

  <ul class="job-list col-a">
    <li><svg class="tick" width="13" height="11"><use href="#tick-mark"/></svg>BI Developer</li>
    <li><svg class="tick" width="13" height="11"><use href="#tick-mark"/></svg>Data Analyst</li>
    <li><svg class="tick" width="13" height="11"><use href="#tick-mark"/></svg>Data Scientist</li>
  </ul>
  <ul class="job-list col-b">
    <li><svg class="tick" width="13" height="11"><use href="#tick-mark"/></svg>Data Developer</li>
    <li><svg class="tick" width="13" height="11"><use href="#tick-mark"/></svg>Computer Systems Analyst</li>
    <li><svg class="tick" width="13" height="11"><use href="#tick-mark"/></svg>Financial Analyst</li>
  </ul>

  <div class="portrait" role="img" aria-label="Photo of a smiling young professional in a white shirt holding a tablet"></div>

  <svg class="chevrons" width="22" height="70" viewBox="0 0 22 70" aria-hidden="true">
    <g fill="none" stroke="#7fb2f5" stroke-width="4" stroke-linecap="round" stroke-linejoin="round">
      <path d="M3 3 L11 10 L19 3"/><path d="M3 13 L11 20 L19 13"/>
      <path d="M3 43 L11 50 L19 43"/><path d="M3 53 L11 60 L19 53"/>
    </g>
  </svg>

  <h3 class="hired-title">Graduates<br>were hired<br>at:</h3>
  <ul class="hire-list">
    <li><svg class="tick" width="13" height="11"><use href="#tick-mark"/></svg>Veltran</li>
    <li><svg class="tick" width="13" height="11"><use href="#tick-mark"/></svg>Corbel</li>
    <li><svg class="tick" width="13" height="11"><use href="#tick-mark"/></svg>Norvik</li>
    <li><svg class="tick" width="13" height="11"><use href="#tick-mark"/></svg>Aurevo</li>
    <li><svg class="tick" width="13" height="11"><use href="#tick-mark"/></svg>Stellwick</li>
  </ul>

  <div class="footer-band"></div>
</main>
</body>
</html>
```